Proposal Microsoft Word Template

We are looking for a professional, 5 page document to import our proposals onto. We are looking for a cover page with plenty of color and design built around and utilizing our logo. The remaining four pages should utilize our logo and have some design elements to make it stand apart from other formal proposals. We aren't sure what this looks like yet, so we are open to plenty of ideas. I will upload our logo for your use. We are a fire protection company that sells primarily to other commercial clientele.

First page will be the cover page. This should have our logo prominently placed. A place for the clients name and info.
Second page will be the Executive Summary. Smaller logo, possibly a border on this page, and a clean colorful ribbon on the footer with our information on the bottom. I do like red, blue and black for colors.

Third page will be material lists and pricing information

4th page will consist of detailed scope of work, and exclusions
Fifth page will consist of terms and conditions

Target Market(s)

Commercial Industrial Government Sectors

Requirements
Must have
• Color, clean lines and formatting.

```html
<!DOCTYPE html>
<html lang="en">
<head>
<meta charset="utf-8">
<title>Bastion Fire and Security – Proposal Template</title>
<link rel="stylesheet" href="https://fonts.googleapis.com/css2?family=Oswald:wght@600;700&family=Lato:wght@400;700&display=swap">
<style>
:root{
  --red:#b0232a;
  --red-bright:#c8252c;
  --charcoal:#3d3d3d;
  --ink:#222222;
  --body:#333333;
  --muted:#8a8a8a;
  --row:#efefef;
  --canvas:#c4c4c4;
  --gold:#f2b705;
  --white:#ffffff;
}
*{box-sizing:border-box;margin:0;padding:0}
html,body{width:1200px;height:1110px;overflow:hidden;background:var(--canvas)}
body{position:relative;font-family:"Lato",Arial,sans-serif;color:var(--body)}
.page{position:absolute;width:384px;height:544px;background:var(--white);overflow:hidden;box-shadow:0 1px 3px rgba(0,0,0,.25)}
.page--cover{left:0;top:0}
.page--summary{left:408px;top:0}
.page--pricing{left:816px;top:0}
.page--scope{left:0;top:566px}
.page--contact{left:408px;top:566px;background:var(--charcoal)}
.abs{position:absolute}
.page-title{position:absolute;left:25px;top:20px;font-family:"Oswald",Impact,sans-serif;font-weight:700;font-size:15px;letter-spacing:.3px;color:var(--red)}
.body-copy{position:absolute;font-size:5.6px;line-height:9.3px;text-align:justify;color:var(--body)}
.body-copy p+p{margin-top:7px}
.footer-band{position:absolute;left:0;bottom:0;width:100%;height:17px;background:var(--red)}
.page-num{position:absolute;right:28px;top:4px;font-size:5.5px;color:var(--white)}
.brand{position:absolute;font-family:"Oswald",Impact,sans-serif;font-weight:700;color:var(--red);text-transform:uppercase;line-height:1.05;letter-spacing:.6px}
.brand--sm{font-size:10px;width:100px}
.brand--lg{font-size:15px;width:140px;text-align:right}
/* cover */
.cover-title{position:absolute;left:25px;top:21px;font-family:"Oswald",Impact,sans-serif;font-weight:700;font-size:19px;color:var(--ink);letter-spacing:.3px}
.cover-subtitle{position:absolute;left:25px;top:49px;font-size:11px;color:#555}
.cover-photo{position:absolute;left:0;top:84px;width:384px;height:390px;background:linear-gradient(100deg,#f7b21c 0%,#e8690e 35%,#7a3b14 62%,#3b2a18 80%,#e48a1c 100%)}
/* summary */
.sub-heading{position:absolute;left:25px;top:215px;font-family:"Oswald",Impact,sans-serif;font-weight:600;font-size:6.5px;color:var(--red)}
.quote-band{position:absolute;left:0;top:378px;width:384px;height:102px;background:var(--charcoal);color:var(--white);text-align:center}
.quote-mark{font-family:Georgia,serif;font-size:14px;font-weight:700;line-height:1}
.quote-text{margin:4px 25px 0;font-size:7.2px;line-height:11.2px;text-align:justify}
/* pricing */
.product-row{position:absolute;left:0;width:384px;height:71px}
.product-row svg{position:absolute;left:0;top:0}
.thumb{position:absolute;left:26px;top:7px;width:61px;height:61px;background:var(--white);border:1px solid #bbb;box-shadow:0 1px 2px rgba(0,0,0,.2);font-size:6.5px;line-height:8px;text-align:center;color:#333;padding-top:22px}
.product-name{position:absolute;left:97px;top:9px;font-size:7.3px;font-weight:700;color:var(--ink)}
.price{position:absolute;left:266px;top:2px;height:14px;padding:0 4px;font-size:8px;line-height:14px;font-weight:700;color:var(--white);background:var(--red)}
.product-desc{position:absolute;left:97px;top:21px;width:216px;font-size:5.3px;line-height:7.7px;text-align:justify;color:var(--muted)}
.product-row--featured .product-name{color:var(--white)}
.product-row--featured .product-desc{color:#b5b5b5}
.product-row--featured .price{background:var(--gold);color:#222}
/* scope */
.scope-photo{position:absolute;left:0;top:79px;width:130px;height:401px;background:linear-gradient(180deg,#f2a30f 0%,#e4720b 45%,#a0380a 80%,#2a1208 100%)}
.callout{position:absolute;left:146px;top:355px;width:238px;height:125px;background:var(--charcoal);color:var(--white);padding:15px 26px 0 26px;font-size:7.2px;line-height:11.1px;text-align:justify}
/* contact */
.contact-title{position:absolute;left:0;top:22px;width:100%;text-align:center;font-family:"Oswald",Impact,sans-serif;font-weight:700;font-size:14px;color:var(--white)}
.contact-copy{color:#e6e6e6;left:25px;top:81px;width:334px}
.contact-item{position:absolute;left:0;width:100%;text-align:center;font-size:7.2px;color:var(--white)}
.contact-icon{display:block;margin:0 auto 6px;width:22px;height:22px}
.page--contact .brand{color:#9a9a9a;left:122px;top:492px;width:140px;text-align:center}
</style>
</head>
<body>

<!-- Cover -->
<section class="page page--cover">
  <h1 class="cover-title">PROJECT TITLE GOES HERE</h1>
  <p class="cover-subtitle">Project subtitle goes here</p>
  <div class="cover-photo" role="img" aria-label="Photo of firefighters in helmets and turnout gear spraying water into a large blaze"></div>
  <div class="brand brand--lg" style="left:219px;top:486px">Bastion<br>Fire and Security</div>
</section>

<!-- Executive summary -->
<section class="page page--summary">
  <h2 class="page-title">PAGE TITLE GOES HERE</h2>
  <div class="body-copy" style="left:25px;top:79px;width:334px">
    <p>Lorem ipsum dolor sit amet, consectetur adipiscing elit, sed do eiusmod tempor incididunt ut labore et dolore magna aliqua. Ut enim ad minim veniam, quis nostrud exercitation ullamco laboris nisi ut aliquip ex ea commodo consequat. Duis aute irure dolor in reprehenderit in voluptate velit esse cillum dolore eu fugiat nulla pariatur. Excepteur sint occaecat cupidatat non proident, sunt in culpa qui officia deserunt mollit anim id est laborum.</p>
    <p>Sed ut perspiciatis unde omnis iste natus error sit voluptatem accusantium doloremque laudantium, totam rem aperiam, eaque ipsa quae ab illo inventore veritatis et quasi architecto beatae vitae dicta sunt explicabo. Nemo enim ipsam voluptatem quia voluptas sit aspernatur aut odit aut fugit, sed quia consequuntur magni dolores eos qui ratione voluptatem sequi nesciunt. Neque porro quisquam est, qui dolorem ipsum quia dolor sit amet, consectetur, adipisci velit, sed quia non numquam eius modi tempora incidunt ut labore et dolore magnam aliquam quaerat voluptatem. Ut enim ad minima veniam, quis nostrum exercitationem ullam corporis suscipit laboriosam, nisi ut aliquid ex ea commodi consequatur? Quis autem vel eum iure reprehenderit qui in ea voluptate velit esse quam nihil molestiae consequatur, vel illum qui dolorem eum fugiat quo voluptas nulla pariatur?</p>
  </div>
  <h3 class="sub-heading">TEXT TITLE</h3>
  <div class="body-copy" style="left:25px;top:228px;width:158px">
    <p>Lorem ipsum dolor sit amet, consectetur adipiscing elit, sed do eiusmod tempor incididunt ut labore et dolore magna aliqua. Ut enim ad minim veniam, quis nostrud exercitation ullamco laboris nisi ut aliquip ex ea commodo consequat. Duis aute irure dolor in reprehenderit in voluptate velit esse cillum dolore eu fugiat nulla pariatur. Excepteur sint occaecat cupidatat non proident, sunt in culpa qui officia deserunt mollit anim id est laborum.</p>
    <p>Sed ut perspiciatis unde omnis iste natus error sit voluptatem accusantium doloremque laudantium, totam rem aperiam, eaque ipsa quae ab illo inventore veritatis et quasi architecto beatae vitae dicta sunt</p>
  </div>
  <div class="body-copy" style="left:201px;top:228px;width:158px">
    <p>explicabo. Nemo enim ipsam voluptatem quia voluptas sit aspernatur aut odit aut fugit, sed quia consequuntur magni dolores eos qui ratione voluptatem sequi nesciunt. Neque porro quisquam est, qui dolorem ipsum quia dolor sit amet, consectetur, adipisci velit, sed quia non numquam eius modi tempora incidunt ut labore et dolore magnam aliquam quaerat voluptatem. Ut enim ad minima veniam, quis nostrum exercitationem ullam corporis suscipit laboriosam, nisi ut aliquid ex ea commodi consequatur? Quis autem vel eum iure reprehenderit qui in ea voluptate velit esse quam nihil molestiae consequatur, vel illum qui dolorem eum fugiat quo voluptas nulla pariatur?</p>
  </div>
  <blockquote class="quote-band">
    <div class="quote-mark" style="margin-top:9px">&ldquo;</div>
    <p class="quote-text">Lorem ipsum dolor sit amet, consectetur adipiscing elit, sed do eiusmod tempor incididunt ut labore et dolore magna aliqua. Ut enim ad minim veniam, quis nostrud exercitation ullamco laboris nisi ut aliquip ex ea commodo consequat. Duis aute irure dolor in voluptate velit esse cillum dolore eu fugiat nulla pariatur. Excepteur sint occaecat cupidatat non proident, sunt in culpa qui officia deserunt mollit anim id est laborum.</p>
    <div class="quote-mark" style="margin-top:2px">&rdquo;</div>
  </blockquote>
  <div class="brand brand--sm" style="left:25px;top:498px">Bastion<br>Fire and Security</div>
  <div class="footer-band"><span class="page-num">02</span></div>
</section>

<!-- Pricing -->
<section class="page page--pricing">
  <h2 class="page-title">PAGE TITLE GOES HERE</h2>

  <div class="product-row product-row--featured" style="top:78px;height:72px">
    <svg width="384" height="72" viewBox="0 0 384 72"><polygon points="0,0 359,0 326,36 359,72 0,72" fill="#3d3d3d"/></svg>
    <div class="thumb">Image place<br>holder</div>
    <div class="product-name">Name of the product</div>
    <div class="price">$1,500</div>
    <p class="product-desc">Lorem ipsum dolor sit amet, consectetur adipiscing elit, sed do eiusmod tempor incididunt ut labore et dolore magna aliqua. Ut enim ad minim veniam, quis nostrud exercitation ullamco laboris nisi ut aliquip ex ea commodo consequat. Duis aute irure dolor in reprehenderit in voluptate velit esse cillum dolore eu fugiat nulla pariatur.</p>
  </div>

  <div class="product-row" style="top:161px">
    <svg width="384" height="71" viewBox="0 0 384 71"><polygon points="0,0 359,0 345,71 0,71" fill="#efefef"/></svg>
    <div class="thumb">Image place<br>holder</div>
    <div class="product-name">Name of the product</div>
    <div class="price">$1,500</div>
    <p class="product-desc">Lorem ipsum dolor sit amet, consectetur adipiscing elit, sed do eiusmod tempor incididunt ut labore et dolore magna aliqua. Ut enim ad minim veniam, quis nostrud exercitation ullamco laboris nisi ut aliquip ex ea commodo consequat. Duis aute irure dolor in reprehenderit in voluptate velit esse cillum dolore eu fugiat nulla pariatur.</p>
  </div>

  <div class="product-row" style="top:244px">
    <svg width="384" height="71" viewBox="0 0 384 71"><polygon points="0,0 359,0 345,71 0,71" fill="#efefef"/></svg>
    <div class="thumb">Image place<br>holder</div>
    <div class="product-name">Name of the product</div>
    <div class="price">$1,500</div>
    <p class="product-desc">Lorem ipsum dolor sit amet, consectetur adipiscing elit, sed do eiusmod tempor incididunt ut labore et dolore magna aliqua. Ut enim ad minim veniam, quis nostrud exercitation ullamco laboris nisi ut aliquip ex ea commodo consequat. Duis aute irure dolor in reprehenderit in voluptate velit esse cillum dolore eu fugiat nulla pariatur.</p>
  </div>

  <div class="product-row" style="top:327px">
    <svg width="384" height="71" viewBox="0 0 384 71"><polygon points="0,0 359,0 345,71 0,71" fill="#efefef"/></svg>
    <div class="thumb">Image place<br>holder</div>
    <div class="product-name">Name of the product</div>
    <div class="price">$1,500</div>
    <p class="product-desc">Lorem ipsum dolor sit amet, consectetur adipiscing elit, sed do eiusmod tempor incididunt ut labore et dolore magna aliqua. Ut enim ad minim veniam, quis nostrud exercitation ullamco laboris nisi ut aliquip ex ea commodo consequat. Duis aute irure dolor in reprehenderit in voluptate velit esse cillum dolore eu fugiat nulla pariatur.</p>
  </div>

  <div class="product-row" style="top:410px">
    <svg width="384" height="71" viewBox="0 0 384 71"><polygon points="0,0 359,0 345,71 0,71" fill="#efefef"/></svg>
    <div class="thumb">Image place<br>holder</div>
    <div class="product-name">Name of the product</div>
    <div class="price">$1,500</div>
    <p class="product-desc">Lorem ipsum dolor sit amet, consectetur adipiscing elit, sed do eiusmod tempor incididunt ut labore et dolore magna aliqua. Ut enim ad minim veniam, quis nostrud exercitation ullamco laboris nisi ut aliquip ex ea commodo consequat. Duis aute irure dolor in reprehenderit in voluptate velit esse cillum dolore eu fugiat nulla pariatur.</p>
  </div>

  <div class="brand brand--sm" style="left:25px;top:498px">Bastion<br>Fire and Security</div>
  <div class="footer-band"><span class="page-num">03</span></div>
</section>

<!-- Scope of work -->
<section class="page page--scope">
  <h2 class="page-title">PAGE TITLE GOES HERE</h2>
  <div class="scope-photo" role="img" aria-label="Photo of a firefighter in silhouette standing before a wall of orange flames"></div>
  <div class="body-copy" style="left:146px;top:80px;width:214px">
    <p>Lorem ipsum dolor sit amet, consectetur adipiscing elit, sed do eiusmod tempor incididunt ut labore et dolore magna aliqua. Ut enim ad minim veniam, quis nostrud exercitation ullamco laboris nisi ut aliquip ex ea commodo consequat. Duis aute irure dolor in reprehenderit in voluptate velit esse cillum dolore eu fugiat nulla pariatur. Excepteur sint occaecat cupidatat non proident, sunt in culpa qui officia deserunt mollit anim id est laborum.</p>
    <p>Sed ut perspiciatis unde omnis iste natus error sit voluptatem accusantium doloremque laudantium, totam rem aperiam, eaque ipsa quae ab illo inventore veritatis et quasi architecto beatae vitae dicta sunt explicabo. Nemo enim ipsam voluptatem quia voluptas sit aspernatur aut odit aut fugit, sed quia consequuntur magni dolores eos qui ratione voluptatem sequi nesciunt. Neque porro quisquam est, qui dolorem ipsum quia dolor sit amet, consectetur, adipisci velit, sed quia non numquam eius modi tempora incidunt ut labore et dolore magnam aliquam quaerat voluptatem. Ut enim ad minima veniam, quis nostrum exercitationem ullam corporis suscipit laboriosam, nisi ut aliquid ex ea commodi consequatur? Quis autem vel eum iure reprehenderit qui in ea voluptate velit esse quam nihil molestiae consequatur, vel illum qui dolorem eum fugiat quo voluptas nulla pariatur?</p>
    <p>Lorem ipsum dolor sit amet, consectetur adipiscing elit, sed do eiusmod tempor incididunt ut labore et dolore magna aliqua. Ut enim ad minim veniam, quis nostrud exercitation ullamco laboris nisi ut aliquip ex ea commodo consequat. Duis aute irure dolor in reprehenderit in voluptate velit esse cillum dolore eu fugiat nulla pariatur. Excepteur sint occaecat cupidatat non proident, sunt in culpa qui officia deserunt mollit anim id est laborum.</p>
  </div>
  <div class="callout">Lorem ipsum dolor sit amet, consectetur adipiscing elit, sed do eiusmod tempor incididunt ut labore et dolore magna aliqua. Ut enim ad minim veniam, quis nostrud exercitation ullamco laboris nisi ut aliquip ex ea commodo consequat. Duis aute irure dolor in reprehenderit in voluptate velit esse cillum dolore eu fugiat nulla pariatur. Excepteur sint occaecat cupidatat non proident, sunt in culpa qui officia deserunt mollit anim id est laborum.</div>
  <div class="brand brand--sm" style="left:25px;top:498px">Bastion<br>Fire and Security</div>
  <div class="footer-band"><span class="page-num">04</span></div>
</section>

<!-- Contact -->
<section class="page page--contact">
  <h2 class="contact-title">CONTACT US</h2>
  <div class="body-copy contact-copy">
    <p>Lorem ipsum dolor sit amet, consectetur adipiscing elit, sed do eiusmod tempor incididunt ut labore et dolore magna aliqua. Ut enim ad minim veniam, quis nostrud exercitation ullamco laboris nisi ut aliquip ex ea commodo consequat. Duis aute irure dolor in reprehenderit in voluptate velit esse cillum dolore eu fugiat nulla pariatur. Excepteur sint occaecat cupidatat non proident, sunt in culpa qui officia deserunt mollit anim id est laborum.</p>
    <p>Sed ut perspiciatis unde omnis iste natus error sit voluptatem accusantium doloremque laudantium, totam rem aperiam, eaque ipsa quae ab illo inventore veritatis et quasi architecto beatae vitae dicta sunt explicabo. Nemo enim ipsam voluptatem quia voluptas sit aspernatur aut odit aut fugit, sed quia consequuntur magni dolores eos qui ratione voluptatem sequi nesciunt. Neque porro quisquam est, qui dolorem ipsum quia dolor sit amet, consectetur, adipisci velit, sed quia non numquam eius modi tempora incidunt ut labore et dolore magnam aliquam quaerat voluptatem. Ut enim ad minima veniam, quis nostrum exercitationem ullam corporis suscipit laboriosam, nisi ut aliquid ex ea commodi consequatur?</p>
  </div>

  <div class="contact-item" style="top:198px">
    <svg class="contact-icon" viewBox="0 0 22 22"><circle cx="11" cy="11" r="11" fill="#c8252c"/><circle cx="11" cy="11" r="6.5" fill="none" stroke="#fff" stroke-width=".8"/><path d="M8.6 7.9c.4-.4.9-.3 1.1.1l.6 1.1c.2.4 0 .7-.3.9-.2.2 0 .8.6 1.4s1.2.8 1.4.6c.2-.3.5-.5.9-.3l1.1.6c.4.2.5.7.1 1.1-.9.9-2.4.5-3.9-1s-2.1-3.1-1.2-3.9z" fill="none" stroke="#fff" stroke-width=".8"/></svg>
    123.456.789
  </div>
  <div class="contact-item" style="top:262px">
    <svg class="contact-icon" viewBox="0 0 22 22"><circle cx="11" cy="11" r="11" fill="#c8252c"/><circle cx="11" cy="11" r="6.5" fill="none" stroke="#fff" stroke-width=".8"/><rect x="7.7" y="8.7" width="6.6" height="4.6" fill="none" stroke="#fff" stroke-width=".8"/><path d="M7.7 8.7 11 11.3 14.3 8.7" fill="none" stroke="#fff" stroke-width=".8"/></svg>
    hello@bastionfiresecurity.com
  </div>
  <div class="contact-item" style="top:334px">
    <svg class="contact-icon" viewBox="0 0 22 22"><circle cx="11" cy="11" r="11" fill="#c8252c"/><circle cx="11" cy="11" r="6.5" fill="none" stroke="#fff" stroke-width=".8"/><circle cx="11" cy="11" r="3.6" fill="none" stroke="#fff" stroke-width=".8"/><path d="M7.4 11h7.2M11 7.4c-1.4 2.2-1.4 5 0 7.2M11 7.4c1.4 2.2 1.4 5 0 7.2" fill="none" stroke="#fff" stroke-width=".7"/></svg>
    www.bastionfiresecurity.com
  </div>
  <div class="contact-item" style="top:404px">
    <svg class="contact-icon" viewBox="0 0 22 22"><circle cx="11" cy="11" r="11" fill="#c8252c"/><circle cx="11" cy="11" r="6.5" fill="none" stroke="#fff" stroke-width=".8"/><path d="M11 14.6s-2.6-2.7-2.6-4.6a2.6 2.6 0 0 1 5.2 0c0 1.9-2.6 4.6-2.6 4.6z" fill="none" stroke="#fff" stroke-width=".8"/><circle cx="11" cy="10" r=".9" fill="#fff"/></svg>
    123, Example street, Example
  </div>

  <div class="brand brand--lg">Bastion<br>Fire and Security</div>
</section>

</body>
</html>
```